Business Card Design Project

looking for business cards with new logo

I am looking to keep with the colors of the logo i posted.  Here are some other details to consider.  I would like my website prominently displayed on the business card with the logo.  my website is www.PRopelVK.com...it should be spelled this way.

My contact information is:

Daniel J Whitcombe III
Broker/Owner
4587 Larkspur Ave., Suite 308
Marlow Springs, Texas 76520
Office: 830-419-5576
Email:  Daniel@PRopelVK.com

Thank you
Daniel Whitcombe

```html
<!DOCTYPE html>
<html lang="en">
<head>
<meta charset="utf-8">
<title>Propel Realty Business Card</title>
<link rel="stylesheet" href="https://fonts.googleapis.com/css2?family=Open+Sans:wght@400;600&family=Roboto+Condensed:wght@400;700&display=swap">
<style>
  :root {
    --stage: #1c1c1e;
    --card-light: #0a68b4;
    --card-mid: #0856a0;
    --card-edge: #064585;
    --band-dark: #053a70;
    --band-darker: #042f5e;
    --accent: #27a6ec;
    --text: #ffffff;
    --text-soft: #e6eef7;
  }
  * { box-sizing: border-box; margin: 0; padding: 0; }
  html, body {
    width: 1200px; height: 676px; overflow: hidden;
    background: var(--stage);
  }
  .canvas {
    position: relative; width: 1200px; height: 676px;
    display: flex; align-items: center; justify-content: center; gap: 50px;
  }
  .card {
    position: relative; width: 525px; height: 300px; overflow: hidden;
    border-radius: 3px;
    box-shadow: 0 12px 30px rgba(0,0,0,.55);
  }
  /* Front */
  .card-front {
    background: radial-gradient(ellipse at 45% 40%, var(--card-light) 0%, var(--card-mid) 45%, var(--card-edge) 100%);
    display: flex; flex-direction: column; align-items: center; justify-content: center;
  }
  .brand-name {
    font-family: "Open Sans", sans-serif; font-weight: 600;
    color: var(--text); font-size: 52px; letter-spacing: -0.5px; line-height: 1;
    display: flex; align-items: center; gap: 14px; white-space: nowrap;
  }
  .brand-mark {
    width: 16px; height: 16px; background: var(--accent); flex: none;
  }
  .front-website {
    margin-top: 34px;
    font-family: "Roboto Condensed", sans-serif; font-weight: 400;
    color: var(--accent); font-size: 17px; letter-spacing: 4px; text-transform: uppercase;
  }
  /* Back */
  .card-back {
    background: radial-gradient(ellipse at 60% 20%, var(--card-light) 0%, var(--card-mid) 55%, var(--card-edge) 100%);
  }
  .back-lower {
    position: absolute; left: 0; right: 0; top: 150px; bottom: 0;
    background: linear-gradient(180deg, var(--band-dark) 0%, var(--band-darker) 100%);
  }
  .back-brand {
    position: absolute; left: 32px; top: 34px;
  }
  .back-brand .brand-name { font-size: 36px; gap: 10px; }
  .back-brand .brand-mark { width: 12px; height: 12px; }
  .holder {
    position: absolute; right: 30px; top: 92px; text-align: right;
    font-family: "Roboto Condensed", sans-serif;
  }
  .holder-name { color: var(--text); font-weight: 700; font-size: 26px; line-height: 1.1; white-space: nowrap; }
  .holder-title { color: var(--accent); font-weight: 400; font-size: 19px; margin-top: 6px; }
  .address {
    position: absolute; left: 32px; top: 176px;
    display: flex; gap: 8px; font-style: normal;
    font-family: "Open Sans", sans-serif; font-size: 12.5px; line-height: 1.5; color: var(--text-soft);
  }
  .contacts {
    position: absolute; right: 30px; top: 196px; list-style: none;
    font-family: "Open Sans", sans-serif; font-size: 13px; color: var(--text-soft);
  }
  .contacts li { display: flex; align-items: center; gap: 10px; height: 24px; white-space: nowrap; }
  .icon { width: 13px; height: 13px; flex: none; fill: none; stroke: var(--accent); stroke-width: 1.6; }
  .icon-solid { fill: var(--accent); stroke: none; }
</style>
</head>
<body>
<main class="canvas">
  <section class="card card-front" aria-label="Card front">
    <div class="brand-name"><span class="brand-mark"></span>Propel Realty</div>
    <div class="front-website">www.PRopelVK.com</div>
  </section>

  <section class="card card-back" aria-label="Card back">
    <div class="back-lower"></div>
    <div class="back-brand">
      <div class="brand-name"><span class="brand-mark"></span>Propel Realty</div>
    </div>
    <div class="holder">
      <div class="holder-name">Daniel J Whitcombe</div>
      <div class="holder-title">Broker / Owner</div>
    </div>
    <address class="address">
      <svg class="icon icon-solid" viewBox="0 0 12 16" style="margin-top:2px"><path d="M6 0a5 5 0 0 0-5 5c0 4 5 11 5 11s5-7 5-11a5 5 0 0 0-5-5zm0 7a2 2 0 1 1 0-4 2 2 0 0 1 0 4z"/></svg>
      <span>4587 Larkspur Ave., Suite 308<br>Marlow Springs, Texas 76520.</span>
    </address>
    <ul class="contacts">
      <li>
        <svg class="icon icon-solid" viewBox="0 0 16 16"><path d="M3.6 1l2.3 2.6-1.3 2a9 9 0 0 0 5.8 5.8l2-1.3L15 12.4 13.6 15C6.5 15 1 9.5 1 2.4z"/></svg>
        <span>830-419-5576</span>
      </li>
      <li>
        <svg class="icon" viewBox="0 0 16 16"><rect x="1.5" y="4" width="13" height="9"/><path d="M1.5 4l6.5 5 6.5-5"/></svg>
        <span>Daniel@PRopelVK.com</span>
      </li>
      <li>
        <svg class="icon" viewBox="0 0 16 16"><circle cx="8" cy="8" r="6.5"/><ellipse cx="8" cy="8" rx="2.8" ry="6.5"/><path d="M1.5 8h13"/></svg>
        <span>www.PRopelVK.com</span>
      </li>
    </ul>
  </section>
</main>
</body>
</html>
```